Dovanne Luxury Landscapes

A landscape business card.

Target Market(s)

Middle aged and up. Professionals.

Industry/Entity Type

Landscape

Contact Information for Business Card

Waverley

Colors
0054AA
0677BA
7BADD7
CADEEF
E8F1F8
0094D4
00A9DD
6FCCEA
C7EBF8
E9F6FB

Requirements
Must have
• The color blue and silver be very attractive
Nice to have
• An embossed logo. A watermark of a plant or something that indicates that we are a landscape company in the background of the backside where list of services are offered. . List of services on the back.
Should not have
• Red, yellow, orange.

```html
<!DOCTYPE html>
<html lang="en">
<head>
<meta charset="utf-8">
<title>Dovanne Luxury Landscapes — Business Card</title>
<link rel="stylesheet" href="https://fonts.googleapis.com/css2?family=Lato:wght@400;700;900&display=swap">
<style>
  :root {
    --backdrop: #242424;
    --card-blue: #0619c4;
    --card-edge: #4a4a52;
    --emboss-ink: #0b1166;
    --emboss-light: rgba(255, 255, 255, 0.14);
    --silver: #f2f4fa;
    --silver-soft: #dfe3f3;
  }
  * { box-sizing: border-box; margin: 0; padding: 0; }
  html, body {
    width: 1200px;
    height: 825px;
    overflow: hidden;
    background: var(--backdrop);
  }
  .canvas {
    position: relative;
    width: 1200px;
    height: 825px;
    display: flex;
    align-items: center;
    justify-content: center;
    gap: 48px;
  }
  .card {
    position: relative;
    width: 536px;
    height: 306px;
    border-radius: 22px;
    background: var(--card-blue);
    box-shadow: 0 3px 0 var(--card-edge), 0 22px 40px rgba(0, 0, 0, 0.55);
    font-family: "Lato", sans-serif;
    overflow: hidden;
  }

  /* Front side */
  .card-front {
    display: flex;
    flex-direction: column;
    align-items: center;
    justify-content: center;
  }
  .front-mark {
    width: 34px;
    height: 34px;
    border-radius: 50%;
    border: 2px solid var(--emboss-ink);
    box-shadow: 0 1px 0 var(--emboss-light);
    margin-bottom: 18px;
  }
  .brand-name {
    color: var(--emboss-ink);
    font-weight: 700;
    text-transform: uppercase;
    text-align: center;
    text-shadow: 0 1px 0 var(--emboss-light);
    line-height: 1.1;
  }
  .brand-name .brand-primary {
    display: block;
    font-size: 44px;
    letter-spacing: 0.06em;
  }
  .brand-name .brand-secondary {
    display: block;
    font-size: 17px;
    letter-spacing: 0.12em;
    margin-top: 2px;
  }

  /* Back side */
  .back-brand {
    position: absolute;
    top: 46px;
    right: 44px;
    color: var(--emboss-ink);
    font-weight: 700;
    font-size: 30px;
    letter-spacing: 0.06em;
    text-transform: uppercase;
    text-shadow: 0 1px 0 var(--emboss-light);
  }
  .contact-block {
    position: absolute;
    left: 40px;
    right: 32px;
    bottom: 34px;
    color: var(--silver);
    text-transform: uppercase;
  }
  .contact-name {
    font-weight: 900;
    font-size: 24px;
    letter-spacing: 0.12em;
    margin-bottom: 6px;
    white-space: nowrap;
  }
  .contact-line {
    font-weight: 400;
    font-size: 11.5px;
    letter-spacing: 0.06em;
    color: var(--silver-soft);
    line-height: 1.55;
    white-space: nowrap;
  }
</style>
</head>
<body>
  <main class="canvas">
    <section class="card card-front" aria-label="Card front">
      <span class="front-mark" aria-hidden="true"></span>
      <h1 class="brand-name">
        <span class="brand-primary">Dovanne</span>
        <span class="brand-secondary">Luxury Landscapes</span>
      </h1>
    </section>

    <section class="card card-back" aria-label="Card back">
      <div class="back-brand">Dovanne</div>
      <div class="contact-block">
        <p class="contact-name">Marla Thibodeau</p>
        <p class="contact-line">47 Kinsac Crest Road, Larchmere, Bramwell County, Z9X 4T2</p>
        <p class="contact-line">555-214-0148 | www.dovanne.com</p>
      </div>
    </section>
  </main>
</body>
</html>
```